Amber Orchard (instructional dating book)

Title: Amber Orchard
Subtitle: Where to plant tulips along a crooked brick path
Author: R.K. Tolvane
I'm seeking the title to be central with the subtitle underneath and the author slightly lower and to the left. Perhaps a border or two around the font. I thought the background could look aged (off color and old textured paper) and the background slightly punched into the texture like a typewriter has been used. I imagine it something like an old Pemberworth playbook or 1940s morse code manual. Many thanks!

Target Market(s)

18 to 45 year old single people

Industry/Entity Type

Dating

Font styles to use
Serif

Requirements
Must have
• Text with border or two
Nice to have
• Traditional feel. The book is instructional.
Should not have
• Too much color or flair

```html
<!DOCTYPE html>
<html lang="en">
<head>
<meta charset="utf-8">
<title>Amber Orchard — Book Cover</title>
<link rel="stylesheet" href="https://fonts.googleapis.com/css2?family=Playfair+Display:ital,wght@0,400;0,700;1,400&display=swap">
<style>
  :root {
    --backdrop: #ece8e1;
    --paper: #d9c8ad;
    --paper-light: #e0d1b8;
    --paper-dark: #cdbb9e;
    --band: #c7b597;
    --ink: #1d1a16;
    --ink-soft: #2b2620;
    --ornament: #8a7a62;
  }
  * { margin: 0; padding: 0; box-sizing: border-box; }
  html, body {
    width: 1200px;
    height: 800px;
    overflow: hidden;
    background: var(--backdrop);
  }
  .canvas {
    position: relative;
    width: 1200px;
    height: 800px;
    display: flex;
    align-items: center;
    justify-content: center;
  }
  .book-cover {
    position: relative;
    width: 510px;
    height: 690px;
    background:
      radial-gradient(ellipse at 30% 20%, var(--paper-light) 0%, transparent 60%),
      radial-gradient(ellipse at 80% 90%, var(--paper-dark) 0%, transparent 55%),
      var(--paper);
    box-shadow: 0 2px 6px rgba(0,0,0,0.12);
  }
  .frame-outer {
    position: absolute;
    inset: 26px;
    border: 2px solid var(--ink);
  }
  .frame-inner {
    position: absolute;
    inset: 35px;
    border: 1px solid var(--ink);
  }
  .title-band {
    position: absolute;
    top: 36px;
    left: 92px;
    right: 36px;
    height: 196px;
    background: var(--band);
  }
  .title {
    position: absolute;
    top: 70px;
    left: 36px;
    right: 36px;
    text-align: center;
    font-family: "Playfair Display", serif;
    font-weight: 400;
    font-size: 62px;
    line-height: 1.05;
    letter-spacing: 0.14em;
    text-transform: uppercase;
    color: var(--ink);
    padding-left: 0.14em;
  }
  .subtitle-block {
    position: absolute;
    top: 268px;
    left: 80px;
    right: 80px;
    text-align: center;
  }
  .rule {
    height: 0;
    border-top: 2px solid var(--ink);
  }
  .subtitle {
    padding: 18px 0 20px;
    font-family: "Playfair Display", serif;
    font-style: italic;
    font-size: 27px;
    line-height: 1.15;
    color: var(--ink-soft);
    letter-spacing: 0.02em;
  }
  .ornament {
    position: absolute;
    top: 432px;
    left: 118px;
    width: 58px;
    height: 24px;
    border-radius: 12px;
    background: var(--ornament);
    opacity: 0.55;
  }
  .author {
    position: absolute;
    top: 476px;
    left: 94px;
    font-family: "Playfair Display", serif;
    font-weight: 700;
    font-size: 21px;
    color: var(--ink);
    letter-spacing: 0.01em;
  }
</style>
</head>
<body>
  <main class="canvas">
    <section class="book-cover">
      <div class="title-band"></div>
      <div class="frame-outer"></div>
      <div class="frame-inner"></div>
      <h1 class="title">Amber<br>Orchard</h1>
      <div class="subtitle-block">
        <div class="rule"></div>
        <p class="subtitle">Where to plant tulips<br>along a crooked brick path</p>
        <div class="rule"></div>
      </div>
      <div class="ornament" role="img" aria-label="Small decorative scroll flourish"></div>
      <p class="author">R.K. Tolvane</p>
    </section>
  </main>
</body>
</html>
```